Global social media analytics company needs business card design

We need an updated business card design to align with our new website - plumvantix.com -

I would also like a favicon designed as well.

Target Market(s)

CEOs, CMOs go big companies

Industry/Entity Type

Business

Contact Information for Business Card

Room for the following:
Address
Main telephone
Direct telephone or cell phone
twitter handle

Colors
aaaaaa

Requirements
Must have
• Attention to detail; style.
• Use the logo color from our website - which is gray

```html
<!DOCTYPE html>
<html lang="en">
<head>
<meta charset="utf-8">
<title>plumvantix – business cards</title>
<link rel="stylesheet" href="https://fonts.googleapis.com/css2?family=Mulish:wght@400;700&display=swap">
<style>
  :root {
    --stage: #cdcdcd;
    --card-dark: #3f4040;
    --card-light: #ffffff;
    --ink-dark: #3f4040;
    --ink-light: #ffffff;
    --ink-muted: #e4e4e4;
    --ghost: #4a4b4b;
    --shadow: rgba(0, 0, 0, 0.28);
  }
  * { margin: 0; padding: 0; box-sizing: border-box; }
  html, body {
    width: 1200px;
    height: 1000px;
    overflow: hidden;
    background: var(--stage);
    font-family: "Mulish", "Helvetica Neue", Arial, sans-serif;
  }
  .card {
    position: absolute;
    width: 560px;
    height: 320px;
    overflow: hidden;
    box-shadow: 0 4px 14px var(--shadow);
  }
  .card--back { left: 80px; top: 130px; background: var(--card-dark); color: var(--ink-light); }
  .card--front { left: 560px; top: 530px; background: var(--card-light); color: var(--ink-dark); }

  .brand { display: flex; align-items: center; position: absolute; }
  .brand__dot { border-radius: 50%; flex: none; }
  .brand__name { font-weight: 700; letter-spacing: 0.2px; line-height: 1; }

  .card--back .brand { left: 56px; top: 114px; }
  .card--back .brand__dot { width: 48px; height: 48px; background: var(--ink-light); margin-right: 12px; }
  .card--back .brand__name { font-size: 24px; color: var(--ink-light); }

  .card--front .brand { left: 50%; top: 50%; transform: translate(-50%, -50%); }
  .card--front .brand__dot { width: 88px; height: 88px; background: var(--ink-dark); margin-right: 18px; }
  .card--front .brand__name { font-size: 40px; color: var(--ink-dark); }

  .ghost-brand {
    position: absolute;
    left: 40px;
    top: 208px;
    display: flex;
    align-items: center;
  }
  .ghost-brand__dot { width: 150px; height: 150px; border-radius: 50%; background: var(--ghost); margin-right: 18px; }
  .ghost-brand__name { font-weight: 700; font-size: 72px; color: var(--ghost); line-height: 1; }

  .holder {
    position: absolute;
    left: 58px;
    top: 196px;
    font-weight: 700;
    font-size: 15px;
  }
  .contact {
    position: absolute;
    left: 62px;
    top: 232px;
    list-style: none;
    font-size: 13px;
    color: var(--ink-muted);
  }
  .contact__item { display: flex; align-items: center; height: 20px; }
  .contact__icon { width: 13px; height: 13px; margin-right: 10px; fill: var(--ink-light); flex: none; }
</style>
</head>
<body>

<section class="card card--back" aria-label="Business card, contact side">
  <div class="ghost-brand" aria-hidden="true">
    <span class="ghost-brand__dot"></span>
    <span class="ghost-brand__name">plumvantix</span>
  </div>

  <div class="brand">
    <span class="brand__dot"></span>
    <span class="brand__name">plumvantix</span>
  </div>

  <p class="holder">Name Surname</p>

  <ul class="contact">
    <li class="contact__item">
      <svg class="contact__icon" viewBox="0 0 16 16" aria-hidden="true">
        <path d="M1 6c0-2 3-3.5 7-3.5S15 4 15 6v1.5h-3.5V6H4.5v1.5H1z"/>
        <path d="M4 8.5h8l2 5.5H2z"/>
      </svg>
      000 0000
    </li>
    <li class="contact__item">
      <svg class="contact__icon" viewBox="0 0 16 16" aria-hidden="true">
        <path d="M1 3h14v1.2L8 9 1 4.2z"/>
        <path d="M1 5.6l7 4.8 7-4.8V13H1z"/>
      </svg>
      email@quorrelnet.net.au
    </li>
    <li class="contact__item">
      <svg class="contact__icon" viewBox="0 0 16 16" aria-hidden="true">
        <path d="M8 1a5 5 0 0 0-5 5c0 3.6 5 9 5 9s5-5.4 5-9a5 5 0 0 0-5-5zm0 7a2 2 0 1 1 0-4 2 2 0 0 1 0 4z"/>
      </svg>
      PO Box 0000 Marlowe Vale WA 6100
    </li>
  </ul>
</section>

<section class="card card--front" aria-label="Business card, brand side">
  <div class="brand">
    <span class="brand__dot"></span>
    <span class="brand__name">plumvantix</span>
  </div>
</section>

</body>
</html>
```